月経前症候群(PMS)に悩む女性向けにマニュアル配布をする
オプトLPのファーストビュー画像の制作(PC+スマホ)です。

- 案件名
美容LP(PMS訴求)のファーストビュー制作

- 目的
アドレス登録

- ターゲット
PMSに苦しんでいる20〜40代女性
特にイライラ、食欲増加、むくみ

- 制作範囲
スマホ・PC版のファーストビュー(CTAボタンまで)
CTA付近に、下のオファー内容をPCと書籍のモックアップで入れる

- コピー原稿+レイアウト参考
https://notes.paperlyn-share.net/document/d/7Qx2RbWm9KfTz3LpVn8YcH4sJd6UeA1oGi0NwMkZrXt/edit?usp=sharing

- コピー原稿
イライラ・食欲増加・むくみ
何をやってもよくならないPMSが良くなるマニュアル

- 強調ポイント
PMSが良くなる←下のURL1つ目の画像の「1年で結婚したい」のイメージ
マニュアル←「あなたのための婚活セミナー」
https://hanamori-zuan.jp/25/001-3/

- デザイン参考

- メイン画像:
PMSがよくなってにこやかな女性

- カラー
暖色系

- 納品
・透過PNG
(CTAエリアの入力フォームの前後で2つに分割して書き出していただきます)
・AI or PS, XD(元データ)
暖色系 ※どこかでこの色を使って欲しいです(#542D24)
コンペでは、スマホ版だけでオッケーです。当確後、PC版含めて納品いただければと思います。
モックアップの詳細の記載がないとのコメントをいただきましたが、コピー原稿に掲載があります。
それをPC画面と書籍の2パターンでご制作ください。

よろしくお願いいたします。

クオリティが高く、素敵なデザインだったので選ばせていただきました。
すごくセンスの良いデザイナーさんだと思いました。

とても悩んだので選ぶのに時間がかかってしまい
お待たせしてすみませんでした。
この度は素敵なデザインを本当にありがとうございました。

```html
<!DOCTYPE html>
<html lang="ja">
<head>
<meta charset="UTF-8">
<title>PMSが良くなるマニュアル</title>
<link href="https://fonts.googleapis.com/css2?family=Noto+Sans+JP:wght@400;500;700;900&family=Shippori+Mincho:wght@600;700;800&display=swap" rel="stylesheet">
<style>
:root{
  --brown:#542D24;
  --brown-band:#6b4a40;
  --badge:#ece1d5;
  --pink:#e2486f;
  --pink-deep:#d43563;
  --pink-light:#f06a8c;
  --ink:#3a2a26;
  --panel:#ffffff;
  --field-line:#cfc6c2;
  --field-hint:#b9b1ad;
  --photo-light:#f3ece6;
  --photo-mid:#e8dcd3;
  --photo-deep:#d8c5b8;
}
*{margin:0;padding:0;box-sizing:border-box}
html,body{width:694px;height:1200px;overflow:hidden;background:#fff}
.fv{position:relative;width:694px;height:1200px;overflow:hidden;font-family:"Noto Sans JP",sans-serif;color:var(--ink)}
.hero-photo{position:absolute;inset:0;
  background:linear-gradient(160deg,var(--photo-light) 0%,var(--photo-light) 40%,var(--photo-mid) 70%,var(--photo-deep) 100%);}
.top-band{position:absolute;left:0;top:0;width:694px;height:120px}
.badge{position:absolute;top:24px;height:64px;display:flex;align-items:center;justify-content:center;
  background:var(--badge);border-radius:32px;color:var(--brown);font-weight:700;font-size:27px;letter-spacing:1px}
.badge::after{content:"";position:absolute;bottom:-10px;left:50%;margin-left:-10px;border:10px solid transparent;border-top-color:var(--badge);border-bottom:0}
.badge--irritation{left:18px;width:164px}
.badge--appetite{left:250px;width:186px}
.badge--swelling{left:472px;width:160px}
.lead{position:absolute;left:44px;top:180px;font-size:31px;font-weight:700;color:var(--ink);letter-spacing:1px}
.headline{position:absolute;left:0;top:0;font-family:"Shippori Mincho",serif;color:var(--pink)}
.headline__pms{position:absolute;left:30px;top:232px;font-size:156px;font-weight:800;line-height:1;letter-spacing:-3px;white-space:nowrap}
.headline__pms small{font-size:72px;letter-spacing:0}
.headline__better{position:absolute;left:20px;top:456px;font-size:114px;font-weight:800;line-height:1;white-space:nowrap}
.headline__dots{position:absolute;left:20px;top:432px;display:flex}
.headline__dots span{width:114px;display:flex;justify-content:center}
.headline__dots span::before{content:"";width:12px;height:12px;border-radius:50%;background:var(--pink)}
.headline__manual{position:absolute;left:172px;top:650px;font-size:70px;font-weight:700;line-height:1;letter-spacing:4px;white-space:nowrap}
.offer{position:absolute;left:42px;top:786px;width:652px;height:414px;background:var(--panel)}
.offer__lead{position:absolute;left:24px;top:26px;font-size:25px;font-weight:700;color:var(--ink);letter-spacing:1px}
.offer__title{position:absolute;left:20px;top:74px;font-size:40px;font-weight:900;color:var(--ink);white-space:nowrap}
.offer__title em{font-style:normal;color:var(--pink)}
.offer__field{position:absolute;left:23px;top:151px;width:565px;height:72px;border:2px solid var(--field-line);border-radius:8px;
  display:flex;align-items:center;padding-left:22px;font-size:26px;color:var(--field-hint);background:#fff}
.offer__button{position:absolute;left:22px;top:244px;width:568px;height:104px;border-radius:12px;
  background:linear-gradient(180deg,var(--pink-light) 0%,var(--pink) 50%,var(--pink-deep) 100%);
  box-shadow:0 6px 0 #b02a50;display:flex;align-items:center;justify-content:center;gap:18px;
  color:#fff;font-size:37px;font-weight:900;letter-spacing:1px}
</style>
</head>
<body>
<main class="fv">
  <div class="hero-photo" role="img" aria-label="写真：明るい室内で、PMSが良くなって笑顔を見せるボーダーのトップスの女性"></div>

  <svg class="top-band" viewBox="0 0 694 120" aria-hidden="true">
    <path d="M0 0H694V78Q347 128 0 78Z" fill="var(--brown-band)"/>
  </svg>
  <div class="badge badge--irritation">イライラ</div>
  <div class="badge badge--appetite">食欲増加</div>
  <div class="badge badge--swelling">むくみ</div>

  <p class="lead">何をやってもよくならない</p>

  <h1 class="headline">
    <span class="headline__pms">PMS<small>が</small></span>
    <span class="headline__dots" aria-hidden="true"><span></span><span></span><span></span><span></span></span>
    <span class="headline__better">良くなる</span>
    <span class="headline__manual">マニュアル</span>
  </h1>

  <section class="offer">
    <p class="offer__lead">何をやってもよくならない</p>
    <p class="offer__title">“<em>PMSが良くなる</em>マニュアル”</p>
    <div class="offer__field">メールアドレスを入力してください</div>
    <div class="offer__button">
      <svg width="44" height="44" viewBox="0 0 44 44" aria-hidden="true">
        <circle cx="22" cy="22" r="21" fill="#fff"/>
        <path d="M17 13L31 22L17 31Z" fill="var(--pink)"/>
      </svg>
      今すぐ無料で手に入れる
    </div>
  </section>
</main>
</body>
</html>
```